依頼詳細
道端に掲載する看板デザインの作成をお願い致します。一目で不動産会社だと分かり、シンプルだけどどんな会社か分かるようなデザイン、かつお店に入りやすいようなデザインを希望します。近くに同じような形の看板がありますので、そちらとの見栄えも考えて頂けると選びやすいです(添付データ①)。ちなみに今回考えて頂くのは手前の看板のデザインです(NO.1が書かれてある方)。色の指定はしませんが、弊社のイメージカラーは黒・赤といった感じです。弊社HPのURLも添付致しますので参考までにご覧ください。
看板のサイズは H5650mm × W1240mm です。
記載項目
①会社名:株式会社ミズナギハウス
②ロゴ:添付データ(MIZUNAGI_logo)
③電話番号:0952-47-1958
④矢印(看板の道向かい側に店舗があるため)
希望イメージ
シンプル 複雑
単色 カラフル
暗い 明るい
日常 高級
遊び心 厳粛
未来的 伝統的
女性的 男性的
希望する色
納品ファイル
• 高解像度JPG (.jpg)
• イラストレーター形式 (.ai)
• PNG形式 (.png)
補足説明
弊社HPです。下記リンクよりご覧ください。
https://www.mizunagi-haus.jp/
HP内の「店舗情報」より弊社の店舗の外観・内観も見て頂き、会社の雰囲気を把握して頂ければと思います。
もう少し他のデザインも見て検討したいので締め切りを延長させていただきます。
現看板デザインにもあります、「取扱い物件数&地域密着度No.1」という表記に関してですが、こちらの表記はあっても無くても、どちらでも構いません。
ただ、あった方が会社の魅力をより伝えられると思います。

また、もし表記をする際には「取扱い物件数」の前に「佐賀県西部エリア」という言葉も追加をお願い致します。

他に疑問点があればご質問ください。
締め切り間近での追記申し訳ありません。

提案して頂いているデザインを基に何を一番に売り出した方が良いか弊社の方で再度検討しましたところ、会社名やロゴよりも「賃貸も売買も取り扱っている」という点を強調した方がやはり良いのでは、という結論に至りました。

この意見をまとめ、弊社の方で簡単な画像を作成いたしましたので、こちらを基にデザインの修正をして頂きたいです。(あくまで文字の配置などの参考としてお使いください。)

デザインイメージとしては子供でもお店に行きたがるような可愛らしい感じ。
配色は何パターンか頂けるとありがたいです。

急な追記となりましたが、柔軟に対応して頂けると幸いでございます。
よろしくお願いいたします。

この度は、弊社が募集する看板デザインにたくさんのご提案を頂きましてありがとうございました。

今回のデザインの決め手となったのは「わかりやすさ(見やすさ)」です。
道端にある看板なので、車に乗っている方が見てもすぐにどんなものを取り扱っている店なのか分かるようなデザインにする必要がありました。
ri-na-worksさんのデザインは分かりやすさを重視しつつも可愛らしくなりすぎないデザインで弊社内でも好評でしたので、今回当選とさせていただきました。

大まかな条件や〆切間近での変更にも柔軟にご対応頂きありがとうございました。
今回選ばせていただいたデザイン以外にも良いデザインがたくさんありました。
今後もご縁がありましたら、また皆さんの素敵な作品をご提案頂きたいと思います。
ありがとうございました。

```html
<!DOCTYPE html>
<html lang="ja">
<head>
<meta charset="utf-8">
<title>ミズナギハウス 看板</title>
<link href="https://fonts.googleapis.com/css2?family=M+PLUS+Rounded+1c:wght@500;700;800&family=Noto+Sans+JP:wght@700;900&display=swap" rel="stylesheet">
<style>
  :root {
    --red: #e60012;
    --white: #ffffff;
    --ink: #222222;
    --grey: #555555;
    --frame: #d8d8d8;
    --town-sky: #f4f7ee;
    --town-ground: #bfdc8a;
  }
  html, body {
    margin: 0;
    padding: 0;
    width: 1200px;
    height: 4740px;
    overflow: hidden;
    background: var(--white);
  }
  .signboard {
    position: relative;
    width: 1200px;
    height: 4740px;
    box-sizing: border-box;
    border: 2px solid var(--frame);
    background: var(--white);
    font-family: "M PLUS Rounded 1c", sans-serif;
  }
  .brand-name {
    position: absolute;
    top: 590px;
    left: 0;
    width: 1200px;
    text-align: center;
    font-family: "M PLUS Rounded 1c", sans-serif;
    font-weight: 800;
    font-size: 112px;
    letter-spacing: 10px;
    line-height: 1;
    color: var(--red);
  }
  .brand-tagline {
    position: absolute;
    top: 712px;
    left: 0;
    width: 1200px;
    text-align: center;
    font-weight: 700;
    font-size: 62px;
    letter-spacing: 4px;
    line-height: 1;
    color: var(--grey);
  }
  .house {
    position: absolute;
    top: 0;
    left: 0;
  }
  .headline {
    position: absolute;
    top: 1360px;
    width: 320px;
    margin: 0;
    display: flex;
    flex-direction: column;
    align-items: center;
    font-family: "M PLUS Rounded 1c", sans-serif;
    font-weight: 700;
    font-size: 270px;
    line-height: 270px;
    color: var(--white);
  }
  .headline span { display: block; height: 270px; }
  .headline--sale { left: 240px; }
  .headline--rent { left: 650px; }
  .shop-type {
    position: absolute;
    top: 3080px;
    left: 0;
    width: 1200px;
    text-align: center;
    font-family: "M PLUS Rounded 1c", sans-serif;
    font-weight: 700;
    font-size: 230px;
    letter-spacing: 16px;
    line-height: 1;
    color: var(--white);
  }
  .parking-sign {
    position: absolute;
    top: 3590px;
    left: 230px;
    width: 800px;
    height: 620px;
  }
  .company-name {
    position: absolute;
    top: 4372px;
    left: 0;
    width: 1200px;
    text-align: center;
    font-family: "Noto Sans JP", sans-serif;
    font-weight: 700;
    font-size: 60px;
    line-height: 1;
    color: var(--ink);
  }
  .phone {
    position: absolute;
    top: 4462px;
    left: 0;
    width: 1200px;
    display: flex;
    justify-content: center;
    align-items: center;
    gap: 10px;
    font-family: "Noto Sans JP", sans-serif;
    font-weight: 900;
    font-size: 88px;
    line-height: 1;
    color: var(--ink);
  }
  .phone svg { width: 80px; height: 80px; }
  .town-scene {
    position: absolute;
    left: 2px;
    right: 2px;
    bottom: 2px;
    height: 160px;
    background: linear-gradient(to bottom, var(--town-sky) 0%, var(--town-sky) 72%, var(--town-ground) 72%, var(--town-ground) 100%);
  }
</style>
</head>
<body>
<main class="signboard">
  <div class="brand-name">MIZUNAGI</div>
  <div class="brand-tagline">ちんたい・ばいばい</div>

  <svg class="house" width="1200" height="3500" viewBox="0 0 1200 3500" aria-hidden="true">
    <polygon fill="var(--red)" points="600,888 928,1088 928,920 1032,920 1032,1152 1080,1160 1080,3450 120,3450 120,1160"/>
  </svg>

  <p class="headline headline--rent" aria-label="ちんたい"><span>ち</span><span>ん</span><span>た</span><span>い</span></p>
  <p class="headline headline--sale" aria-label="ばいばい"><span>ば</span><span>い</span><span>ば</span><span>い</span></p>
  <div class="shop-type">専門店</div>

  <svg class="parking-sign" viewBox="0 0 800 620" role="img" aria-label="駐車場 右方向">
    <text x="0" y="590" font-family="Noto Sans JP, sans-serif" font-weight="900" font-size="720" fill="var(--red)">P</text>
    <polygon fill="var(--red)" points="470,240 590,240 590,150 790,300 590,450 590,360 470,360"/>
  </svg>

  <div class="company-name">株式会社ミズナギハウス</div>
  <div class="phone">
    <svg viewBox="0 0 24 24" aria-hidden="true">
      <path fill="var(--ink)" d="M3 8c0-2 4-4 9-4s9 2 9 4v2h-5V8c-1-.6-2.4-1-4-1s-3 .4-4 1v2H3z M7 11h10l3 8H4z M12 13a2.5 2.5 0 1 0 0 5a2.5 2.5 0 1 0 0-5z"/>
    </svg>
    <span>0952-47-1958</span>
  </div>

  <div class="town-scene" role="img" aria-label="家や木、お店が並ぶ可愛らしい街並みのイラスト"></div>
</main>
</body>
</html>
```